The Northmoor Aid League needs a graphic of their innovation approach

What we need?
- we have designed a new innovation approach (see attached). An innovation approach is the process one goes through in order to design and launch a new product or service.
- This new graphic will be used in meetings to help others understand what innovation is and how we do it. It will also be used in training sessions and be the starting point for innovation training materials we are creating
- We have created this draft graphic by copying and pasting new words over another charities innovation process
- We would like you to use your design magic and create our very own innovation process graphic. We would like it to be neat, simple, non fussy, easy to understand /read and in line with our brand colours
Attached:
1. PowerPoint:
- Slide 1: our innovation process
- Slide 2 explanation of process to bring it to life
- Slide 3&4: brand colours
- Slide 5: inspiration / examples of other processes we like the look of
2. Typeface brand guidelines
We can't wait to see what you come up with! Thank you :)
internal employees
Charity

```html
<!DOCTYPE html>
<html lang="en">
<head>
<meta charset="UTF-8">
<title>The Northmoor Aid League – Innovation Approach</title>
<link href="https://fonts.googleapis.com/css2?family=Arimo:wght@700&display=swap" rel="stylesheet">
<style>
  :root {
    --canvas: #fdfdfd;
    --navy: #1c2b45;
    --blue: #1a8bc4;
    --red: #e3191b;
    --orange: #f5a71c;
    --ring: #ececec;
    --disc-light: #fafafa;
    --disc-dark: #e4e4e4;
  }
  html, body {
    margin: 0;
    padding: 0;
    overflow: hidden;
    background: var(--canvas);
  }
  .canvas {
    width: 1200px;
    height: 1000px;
    overflow: hidden;
    background: var(--canvas);
  }
  .process-map { display: block; }
  .milestone-label {
    font-family: "Arimo", Arial, sans-serif;
    font-weight: 700;
    font-size: 20px;
    fill: var(--navy);
  }
  .step-label {
    font-family: "Arimo", Arial, sans-serif;
    font-weight: 700;
    font-size: 16px;
  }
  .phase-title {
    font-family: "Arimo", Arial, sans-serif;
    font-weight: 700;
    font-size: 25px;
  }
  .blue { fill: var(--blue); }
  .red { fill: var(--red); }
  .orange { fill: var(--orange); }
  .track { fill: none; stroke-width: 14; }
  .track-blue { stroke: var(--blue); }
  .track-red { stroke: var(--red); }
  .track-orange { stroke: var(--orange); }
  .phase-ring { fill: none; stroke: var(--ring); stroke-width: 20; }
  .phase-disc { fill: url(#discShade); }
</style>
</head>
<body>
<main class="canvas">
  <svg class="process-map" width="1200" height="1000" viewBox="0 0 1200 1000" aria-label="The Northmoor Aid League innovation approach: Discover, Define, Deliver">
    <defs>
      <radialGradient id="discShade" cx="50%" cy="40%" r="60%">
        <stop offset="0%" stop-color="var(--disc-light)"/>
        <stop offset="100%" stop-color="var(--disc-dark)"/>
      </radialGradient>
    </defs>

    <!-- phase backdrops -->
    <g class="phase-backdrops">
      <circle class="phase-ring" cx="340" cy="498" r="128"/>
      <circle class="phase-ring" cx="600" cy="498" r="128"/>
      <circle class="phase-ring" cx="860" cy="498" r="128"/>
      <circle class="phase-disc" cx="340" cy="498" r="98"/>
      <circle class="phase-disc" cx="600" cy="498" r="98"/>
      <circle class="phase-disc" cx="860" cy="498" r="98"/>
    </g>

    <!-- discover track -->
    <path class="track track-blue" d="M15,498 H208 A132,132 0 0 0 472,498 V492"/>
    <polygon class="blue" points="460,496 472,474 484,496"/>
    <!-- define track -->
    <path class="track track-red" d="M468,498 A132,132 0 0 1 732,498 A132,132 0 0 0 770,592"/>
    <polygon class="red" points="760,582 786,608 782,570"/>
    <!-- deliver track -->
    <path class="track track-orange" d="M780,600 A132,132 0 0 0 992,498 H1140"/>
    <polygon class="orange" points="1138,470 1186,498 1138,526"/>

    <!-- milestones -->
    <g class="milestones">
      <circle class="blue" cx="127" cy="498" r="16"/>
      <circle class="blue" cx="393" cy="610" r="16"/>
      <circle class="red" cx="598" cy="366" r="16"/>
      <circle class="red" cx="712" cy="432" r="16"/>
      <circle class="orange" cx="1055" cy="498" r="16"/>
    </g>

    <text class="milestone-label" x="128" y="472" text-anchor="middle">Challenge</text>
    <text class="milestone-label" x="472" y="647" text-anchor="middle">Opportunity</text>
    <text class="milestone-label" x="472" y="671" text-anchor="middle">Statement</text>
    <text class="milestone-label" x="598" y="343" text-anchor="middle">Concepts</text>
    <text class="milestone-label" x="735" y="419">Pilot</text>
    <text class="milestone-label" x="1055" y="472" text-anchor="middle">Launch</text>

    <!-- step labels -->
    <text class="step-label blue" transform="translate(210,600) rotate(40)">Insight</text>
    <text class="step-label blue" transform="translate(466,602) rotate(-66)">Ideate</text>
    <text class="step-label red" transform="translate(468,430) rotate(-62)">(In) validate</text>
    <text class="step-label red" transform="translate(662,360) rotate(28)">Test</text>
    <text class="step-label red" transform="translate(712,542) rotate(66)">Iterate</text>
    <text class="step-label orange" transform="translate(800,645) rotate(7)">Delivery Plan</text>

    <!-- phase titles -->
    <text class="phase-title blue" x="340" y="538" text-anchor="middle">Discover</text>
    <text class="phase-title red" x="600" y="538" text-anchor="middle">Define</text>
    <text class="phase-title orange" x="860" y="538" text-anchor="middle">Deliver</text>

    <!-- icons -->
    <g class="icon-search" fill="none" stroke="var(--blue)">
      <circle cx="354" cy="460" r="22" stroke-width="3.5"/>
      <path d="M364,448 a13,13 0 0 1 3,14" stroke-width="2.5"/>
      <line x1="338" y1="477" x2="307" y2="500" stroke-width="9" stroke-linecap="round"/>
    </g>
    <g class="icon-target" fill="none" stroke="var(--red)" stroke-width="3">
      <circle cx="592" cy="466" r="30"/>
      <circle cx="592" cy="466" r="20"/>
      <circle cx="592" cy="466" r="10"/>
      <line x1="596" y1="462" x2="638" y2="436" stroke-width="6"/>
      <polygon points="594,463 602,452 606,460" fill="var(--red)" stroke="none"/>
    </g>
    <g class="icon-idea">
      <path d="M842,476 a22,22 0 1 1 34,0 c-4,6 -6,10 -6,16 h-22 c0,-6 -2,-10 -6,-16z" fill="none" stroke="var(--orange)" stroke-width="3"/>
      <rect x="849" y="496" width="20" height="5" fill="var(--orange)"/>
      <rect x="851" y="503" width="16" height="5" fill="var(--orange)"/>
      <g stroke="var(--orange)" stroke-width="2.5" stroke-linecap="round">
        <line x1="859" y1="418" x2="859" y2="428"/>
        <line x1="838" y1="425" x2="843" y2="433"/>
        <line x1="880" y1="425" x2="875" y2="433"/>
      </g>
      <path d="M820,468 q40,10 80,-16" fill="none" stroke="var(--orange)" stroke-width="7" stroke-linecap="round"/>
      <polygon points="892,440 910,444 900,460" fill="var(--orange)"/>
    </g>
  </svg>
</main>
</body>
</html>
```